Vel-Trax.ch is looking for business card letterhead and envelope C5 with WOW effect

We need a strong business card for our company Vel-Trax.ch, logo is available. You want a black or dark background on which the logo Stark r% 26 # 252; appears. Letterhead and envelope in C5 format should be in a similar design, but does not have to be We need a strong business card for our company Vel-Trax.ch, logo is available. A black or dark background is desired, on which the logo Stark comes across. The letterhead and the envelope in C5 format should have a similar design.

Target Market(s)

Private customers as well as entrepreneurs

Contact Information for Business Card

E-mail: info@vel-trax.ch
Web.www.Vel-Trax.ch
Tel: +41 ( 0 ) 79 684 3027
Adresse:
Lindenhaldeweg 14
9403 Brenzikon

Hier kann man Icons verwenden für Email,Tel und Adressse

Font styles to use
Other font styles liked:
• Dubai,bold

Colors

Designer to choose colors to be used in the design.

Requirements
Must have
• WOW effect
Nice to have
• R% 26 # 252; back business card with our service listings. - VEHICLE LABELING - SHOP WINDOW LABELING - STICKERS AND MUCH MORE ... in red color

```html
<!DOCTYPE html>
<html lang="en">
<head>
<meta charset="utf-8">
<title>Vel-Trax.ch – Stationery</title>
<link href="https://fonts.googleapis.com/css2?family=Quicksand:wght@400;500;700&family=Arimo:wght@400;700&display=swap" rel="stylesheet">
<style>
  :root {
    --backdrop: #e6e6e6;
    --paper: #f1f1f1;
    --paper-strip: #e9e9e9;
    --ink: #161616;
    --band: #262626;
    --yellow: #ecbd18;
    --light-text: #e6e6e6;
    --body-text: #8a8a8a;
    --label: #222;
    --emboss: #3b3b3b;
  }
  * { margin: 0; padding: 0; box-sizing: border-box; }
  html, body { width: 1200px; height: 2845px; overflow: hidden; }
  body { background: var(--backdrop); position: relative; font-family: "Quicksand", sans-serif; }

  .sheet { position: absolute; background: var(--paper); box-shadow: 0 12px 26px rgba(0,0,0,0.18); overflow: hidden; }
  .abs { position: absolute; }

  .brand-name { font-family: "Quicksand", sans-serif; font-weight: 700; color: var(--ink); letter-spacing: 1px; white-space: nowrap; }
  .brand-mark { position: absolute; background: var(--yellow); border-radius: 50%; }

  .band { position: absolute; left: 0; width: 100%; background: var(--band); }
  .band-accent { position: absolute; right: 0; top: 0; height: 100%; background: var(--yellow); }

  .contact-line { position: absolute; display: flex; align-items: center; color: var(--light-text); white-space: nowrap; letter-spacing: 1px; }
  .contact-line svg { flex: none; }
  .contact-line .hl { color: var(--yellow); font-weight: 700; }
  .address { position: absolute; color: var(--light-text); letter-spacing: 1.5px; white-space: nowrap; }

  /* business card front */
  .card-front { left: 227px; top: 128px; width: 745px; height: 424px; }
  .card-front .band { top: 233px; height: 167px; }
  .card-front .strip { position: absolute; left: 0; top: 400px; width: 100%; height: 24px; background: var(--paper-strip); }
  .holder-name { position: absolute; left: 27px; top: 246px; font-size: 23px; font-weight: 500; color: var(--yellow); letter-spacing: 1.5px; }
  .holder-role { position: absolute; left: 27px; top: 273px; font-size: 19px; color: var(--light-text); letter-spacing: 1.5px; }
  .card-front .contact-line { font-size: 19px; gap: 10px; left: 27px; }
  .card-front .address { font-size: 19px; left: 294px; line-height: 24px; }

  /* business card back */
  .card-back { left: 227px; top: 632px; width: 745px; height: 426px; background: #1c1c1c; }
  .card-back .texture { position: absolute; inset: 0; background: radial-gradient(ellipse at 55% 75%, #2e2e2e 0%, #1f1f1f 55%, #181818 100%); }
  .card-back .brand-name { color: var(--emboss); font-size: 40px; left: 50%; top: 50%; transform: translate(-50%, -50%); position: absolute; }

  /* letterhead */
  .letterhead { left: 225px; top: 1163px; width: 747px; height: 940px; font-family: "Arimo", sans-serif; }
  .letterhead .band, .envelope .band { height: 66px; }
  .letterhead .band { top: 852px; }
  .small-strip { position: absolute; left: 0; width: 100%; background: var(--paper-strip); }
  .field-label { position: absolute; font-size: 12px; font-weight: 700; color: var(--label); }
  .field-value { position: absolute; font-size: 11px; color: var(--body-text); }
  .salutation { position: absolute; left: 224px; top: 381px; font-size: 15px; color: #7a7a7a; }
  .letter-body { position: absolute; left: 224px; top: 412px; width: 457px; font-size: 11.4px; line-height: 15.8px; color: var(--body-text); text-align: justify; }
  .letter-body p + p { margin-top: 15.8px; }
  .side-note { position: absolute; right: 577px; top: 455px; width: 120px; text-align: right; font-size: 11.4px; line-height: 15.5px; color: var(--body-text); }
  .side-note .lead { color: #444; }
  .side-note p + p { margin-top: 8px; }
  .signature { position: absolute; left: 224px; top: 762px; font-size: 15px; line-height: 19px; color: #7a7a7a; }
  .small-contacts .contact-line { font-family: "Quicksand", sans-serif; font-size: 12.5px; gap: 6px; }
  .small-contacts .address { font-family: "Quicksand", sans-serif; font-size: 12.5px; line-height: 15px; }

  /* envelope */
  .envelope { left: 225px; top: 2182px; width: 747px; height: 528px; }
  .envelope .band { top: 438px; }
</style>
</head>
<body>

<svg width="0" height="0" style="position:absolute">
  <defs>
    <symbol id="icon-phone" viewBox="0 0 20 20">
      <circle cx="10" cy="10" r="10" fill="#ecbd18"/>
      <path d="M5 8 q5-4 10 0 l-1.5 2 -2-1 v-1.2 h-3 v1.2 l-2 1z M6.5 10.5 h7 l1 4 h-9z" fill="#262626"/>
    </symbol>
    <symbol id="icon-mail" viewBox="0 0 20 20">
      <circle cx="10" cy="10" r="10" fill="#ecbd18"/>
      <rect x="4.5" y="6" width="11" height="8" fill="none" stroke="#262626" stroke-width="1.4"/>
      <path d="M4.5 6 l5.5 4.5 5.5-4.5" fill="none" stroke="#262626" stroke-width="1.4"/>
    </symbol>
    <symbol id="icon-web" viewBox="0 0 20 20">
      <circle cx="10" cy="10" r="10" fill="#ecbd18"/>
      <circle cx="10" cy="10" r="5.5" fill="none" stroke="#262626" stroke-width="1.4"/>
      <path d="M4.5 10h11 M10 4.5 q-3 5.5 0 11 q3-5.5 0-11" fill="none" stroke="#262626" stroke-width="1.2"/>
    </symbol>
  </defs>
</svg>

<!-- Business card front -->
<section class="sheet card-front">
  <span class="brand-mark" style="left:70px;top:80px;width:42px;height:42px;"></span>
  <div class="brand-name abs" style="left:148px;top:78px;font-size:38px;">VEL-TRAX.CH</div>
  <div class="band">
    <div class="band-accent" style="width:92px;"></div>
  </div>
  <div class="holder-name">MARCO KELLER</div>
  <div class="holder-role">Managing Director</div>
  <div class="contact-line" style="top:317px;"><svg width="18" height="18"><use href="#icon-phone"/></svg><span>+41 ( 0 ) 79 684 3027</span></div>
  <div class="contact-line" style="top:342px;"><svg width="18" height="18"><use href="#icon-mail"/></svg><span>info@vel-trax.ch</span></div>
  <div class="contact-line" style="top:366px;"><svg width="18" height="18"><use href="#icon-web"/></svg><span>www.<span class="hl">Vel-Trax</span>.ch</span></div>
  <div class="address" style="top:345px;">Lindenhaldeweg 14<br>9412 Brenzikon</div>
  <div class="strip"></div>
</section>

<!-- Business card back -->
<section class="sheet card-back">
  <div class="texture" role="img" aria-label="Dark background with a faint connected-dot network texture"></div>
  <div class="brand-name">VEL-TRAX.CH</div>
</section>

<!-- Letterhead -->
<section class="sheet letterhead">
  <span class="brand-mark" style="left:248px;top:44px;width:36px;height:36px;"></span>
  <div class="brand-name abs" style="left:300px;top:46px;font-size:27px;">VEL-TRAX.CH</div>

  <div class="field-label" style="left:224px;top:286px;">SUBJECT :</div>
  <div class="field-value" style="left:224px;top:302px;">Lorem Ipsum is simply dummy</div>
  <div class="field-label" style="left:618px;top:284px;">DATE :</div>
  <div class="field-value" style="left:618px;top:300px;">15-09-2017</div>

  <div class="salutation">Dear Person,</div>
  <div class="letter-body">
    <p>Lorem Ipsum is simply dummy text of the printing and typesetting industry. Lorem Ipsum has been the industry's standard dummy text ever since the 1500s, when an unknown printer took a galley of type and scrambled it to make a type specimen book. It has survived not only five centuries, but also the leap into electronic typesetting, remaining essentially unchanged. It was popularised in the 1960s with the release of Letraset sheets containing Lorem Ipsum passages, and more recently with desktop publishing software like Aldus PageMaker including versions of Lorem Ipsum.</p>
    <p>Lorem Ipsum is simply dummy text of the printing and typesetting industry. Lorem Ipsum has been the industry's standard dummy text ever since the 1500s, when an unknown printer took a galley of type and scrambled it to make a type specimen book. It has survived not only five centuries, but also the leap into electronic typesetting, remaining essentially unchanged. It was popularised in the 1960s with the release of</p>
    <p>Letraset sheets containing Lorem Ipsum passages, and more recently with desktop publishing software like Aldus PageMaker including versions of Lorem Ipsum.lease of Letraset sheets containing Lorem Ipsum passages, and more recently with desktop publishing software like Aldus PageMaker including versions of Lorem Ipsum. publishing software like Aldus PageMaker including versions of Lorem Ipsum.</p>
  </div>
  <div class="side-note">
    <p><span class="lead">Lorem Ipsum is</span><br>simply dummy text<br>of the printing</p>
    <p><span class="lead">Lorem Ipsum is</span><br>simply dummy text</p>
  </div>
  <div class="signature">Marco Keller<br>Managing Director</div>

  <div class="band small-contacts">
    <div class="band-accent" style="width:52px;"></div>
    <div class="contact-line" style="left:34px;top:10px;"><svg width="12" height="12"><use href="#icon-phone"/></svg><span>+41 ( 0 ) 79 684 3027</span></div>
    <div class="contact-line" style="left:34px;top:25px;"><svg width="12" height="12"><use href="#icon-mail"/></svg><span>info@vel-trax.ch</span></div>
    <div class="contact-line" style="left:34px;top:40px;"><svg width="12" height="12"><use href="#icon-web"/></svg><span>www.<span class="hl">Vel-Trax</span>.ch</span></div>
    <div class="address" style="left:204px;top:25px;">Lindenhaldeweg 14<br>9412 Brenzikon</div>
  </div>
  <div class="small-strip" style="top:918px;height:22px;"></div>
</section>

<!-- Envelope C5 -->
<section class="sheet envelope">
  <span class="brand-mark" style="left:30px;top:62px;width:36px;height:36px;"></span>
  <div class="brand-name abs" style="left:84px;top:64px;font-size:27px;">VEL-TRAX.CH</div>

  <div class="band small-contacts">
    <div class="band-accent" style="width:44px;"></div>
    <div class="contact-line" style="left:28px;top:9px;"><svg width="12" height="12"><use href="#icon-phone"/></svg><span>+41 ( 0 ) 79 684 3027</span></div>
    <div class="contact-line" style="left:28px;top:24px;"><svg width="12" height="12"><use href="#icon-mail"/></svg><span>info@vel-trax.ch</span></div>
    <div class="contact-line" style="left:28px;top:39px;"><svg width="12" height="12"><use href="#icon-web"/></svg><span>www.<span class="hl">Vel-Trax</span>.ch</span></div>
    <div class="address" style="left:188px;top:24px;">Lindenhaldeweg 14<br>9412 Brenzikon</div>
  </div>
  <div class="small-strip" style="top:504px;height:24px;"></div>
</section>

</body>
</html>
```